Need a stunning looking Business Card Design for my Telecom Business, Wow FACTOR!

I deal with high level IT Directors , and Contractors.
I need to impress them with a sleek , professional and unique business card.
Im thinking options as far as rounded edges, plastic , or even metal card or die cut on a corner.
Whatever looks better and leave an unforgettable first impression.
im looking for the wow factor.
Front should have the basics info (attached on the picture of current business card)
i would like to add picture of myself somewhere
Back side
should have logo and maybe some pictures or past projects, you can download from my website ( www.brivelgroup.com)

```html
<!DOCTYPE html>
<html lang="en">
<head>
<meta charset="utf-8">
<title>Brivel Networks – Business Card</title>
<link rel="stylesheet" href="https://fonts.googleapis.com/css2?family=Open+Sans:wght@400;600&family=Work+Sans:wght@800&display=swap">
<style>
  :root {
    --backdrop: #1d1e20;
    --card-deep: #06306f;
    --card-mid: #0a55a6;
    --card-glow: #0c93c9;
    --white: #ffffff;
    --icon-cyan: #2fb4e6;
    --line-red: #e3201f;
    --line-yellow: #f6a914;
    --line-green: #7dbb20;
    --photo-light: #e9ebee;
    --photo-mid: #b9b3b6;
  }
  * { margin: 0; padding: 0; box-sizing: border-box; }
  html, body { width: 1200px; height: 874px; overflow: hidden; }
  body {
    background: var(--backdrop);
    font-family: "Open Sans", sans-serif;
    color: var(--white);
    position: relative;
  }
  .card {
    position: absolute;
    left: 290px;
    width: 620px;
    height: 354px;
    border-radius: 22px;
    overflow: hidden;
    box-shadow: 0 18px 40px rgba(0,0,0,.55);
  }
  /* back side */
  .card--back {
    top: 50px;
    background: radial-gradient(circle at 62% 45%, var(--card-glow) 0%, var(--card-mid) 38%, var(--card-deep) 100%);
  }
  .card__pattern {
    position: absolute; inset: 0;
    background: linear-gradient(135deg, rgba(10,70,160,.35), rgba(20,110,200,.15) 50%, rgba(10,60,150,.35));
  }
  .card--back .brand {
    position: absolute;
    left: 0; right: 0; top: 150px;
    display: flex; justify-content: center; align-items: center; gap: 12px;
  }
  .brand__dot {
    width: 16px; height: 16px; border-radius: 50%;
    background: var(--white);
  }
  .brand__name {
    font-family: "Open Sans", sans-serif;
    font-weight: 600;
    font-size: 38px;
    letter-spacing: 2px;
    text-transform: uppercase;
    color: var(--white);
  }
  /* front side */
  .card--front {
    top: 470px;
    background: radial-gradient(circle at 68% 52%, var(--card-glow) 0%, var(--card-mid) 40%, var(--card-deep) 100%);
  }
  .portrait {
    position: absolute;
    left: 40px; top: 36px;
    width: 108px; height: 108px; border-radius: 50%;
    background: radial-gradient(circle at 50% 40%, var(--photo-light) 0%, var(--photo-light) 45%, var(--photo-mid) 100%);
  }
  .person {
    position: absolute; left: 40px; top: 170px;
  }
  .person__name {
    font-family: "Work Sans", sans-serif;
    font-weight: 800;
    font-size: 26px;
    letter-spacing: 1px;
    text-transform: uppercase;
  }
  .person__role { font-size: 15px; margin-top: 2px; }
  .accent-rule {
    position: absolute; left: 40px; top: 236px;
    width: 540px; height: 4px; display: flex;
  }
  .accent-rule span { height: 100%; }
  .accent-rule .red { width: 32%; background: var(--line-red); }
  .accent-rule .yellow { width: 33%; background: var(--line-yellow); }
  .accent-rule .green { width: 35%; background: var(--line-green); }
  .contacts {
    position: absolute; left: 40px; top: 252px;
    list-style: none; font-size: 14.5px; line-height: 26px;
  }
  .contacts li { display: flex; align-items: center; gap: 9px; }
  .contacts svg { width: 14px; height: 14px; fill: var(--icon-cyan); flex: none; }
  .card--front .brand {
    position: absolute; right: 44px; top: 96px;
    display: flex; align-items: center; gap: 10px;
  }
  .card--front .brand__name { font-size: 28px; }
  .company {
    position: absolute; right: 44px; bottom: 30px;
    text-align: right; font-size: 13.5px; line-height: 20px;
  }
</style>
</head>
<body>

<section class="card card--back" aria-label="Card back">
  <div class="card__pattern" role="img" aria-label="Repeating tone-on-tone brand pattern"></div>
  <div class="brand">
    <span class="brand__dot"></span>
    <span class="brand__name">Brivel Networks</span>
  </div>
</section>

<section class="card card--front" aria-label="Card front">
  <div class="portrait" role="img" aria-label="Portrait photo of Daniel Okada"></div>

  <div class="person">
    <h1 class="person__name">Daniel Okada</h1>
    <p class="person__role">Project Manager / Lead Installer</p>
  </div>

  <div class="accent-rule"><span class="red"></span><span class="yellow"></span><span class="green"></span></div>

  <ul class="contacts">
    <li>
      <svg viewBox="0 0 24 24"><path d="M6.6 10.8c1.4 2.8 3.8 5.1 6.6 6.6l2.2-2.2c.3-.3.7-.4 1-.2 1.1.4 2.3.6 3.6.6.6 0 1 .4 1 1V20c0 .6-.4 1-1 1C10.6 21 3 13.4 3 4c0-.6.4-1 1-1h3.5c.6 0 1 .4 1 1 0 1.3.2 2.5.6 3.6.1.3 0 .7-.2 1z"/></svg>
      (954) 555-0142
    </li>
    <li>
      <svg viewBox="0 0 24 24"><path d="M2 5h20v14H2zm2 2v.5l8 5 8-5V7l-8 5z"/></svg>
      info@brivelgroup.com
    </li>
    <li>
      <svg viewBox="0 0 24 24"><circle cx="12" cy="12" r="10"/></svg>
      brivelgroup.com
    </li>
  </ul>

  <div class="brand">
    <span class="brand__dot"></span>
    <span class="brand__name">Brivel Networks</span>
  </div>

  <address class="company" style="font-style:normal">
    Brivel Networks<br>
    Offices in Miami, Broward &amp; Palm Beach<br>
    Contractor Lic # ES19004826
  </address>
</section>

</body>
</html>
```